Ledgerwell Capital Partners Deck & Brochure

Have a PPT deck and a two page PDF "brochure" that we have to give to clients. Content is there but it could REALLY use some punching up. Including both here because they need to be similar in look and feel

Our website is www.ledgerwellcapitalpartners.example to get a feel for our "design style" so far, including our logo.

Also have a video at video.ledgerwellcapitalpartners.example

Target Market(s)

Large and medium sized corporations, typically a Treasurer

Industry/Entity Type

Management

Requirements
Nice to have
• Movement or animation in the slides of the PPT
Transitions between slides would be nice but it can't be too sassy or take too long

```html
<!DOCTYPE html>
<html lang="en">
<head>
<meta charset="utf-8">
<title>Ledgerwell Capital Partners – Deck Templates</title>
<link href="https://fonts.googleapis.com/css2?family=Arimo:wght@400;700&display=swap" rel="stylesheet">
<style>
  :root {
    --stage: #e8e2d9;
    --brand-brown: #8a7250;
    --bar-light: #c4aa82;
    --bar-dark: #8c7352;
    --title-brown: #8b7355;
    --slide-body: #efefef;
    --slide-footer: #ffffff;
    --ink: #1a1a1a;
    --muted: #8d7d68;
    --navy: #1d3766;
    --bar-blue: #4f81bd;
    --bar-red: #c0504d;
    --bar-green: #9bbb59;
    --bar-purple: #8064a2;
    --grid: #bfbfbf;
  }
  * { margin: 0; padding: 0; box-sizing: border-box; }
  html, body { width: 1200px; height: 800px; overflow: hidden; }
  body {
    background: var(--stage);
    font-family: "Arimo", Arial, sans-serif;
    position: relative;
    color: var(--ink);
  }
  .slide {
    position: absolute;
    width: 362px;
    height: 292px;
    background: var(--slide-body);
    overflow: hidden;
    box-shadow: 0 2px 6px rgba(60, 40, 20, 0.25);
  }
  .slide--cover { left: 23px; top: 45px; background: var(--brand-brown); }
  .slide--bullets { left: 419px; top: 45px; }
  .slide--chart { left: 805px; top: 45px; }
  .slide--sections { left: 29px; top: 430px; }
  .slide--text { left: 425px; top: 430px; }
  .slide--closing { left: 812px; top: 430px; }

  .slide__topbar {
    position: absolute; left: 0; top: 0; width: 100%; height: 13px;
    background: linear-gradient(90deg, var(--bar-light), var(--bar-dark));
  }
  .slide__footer {
    position: absolute; left: 0; bottom: 0; width: 100%; height: 37px;
    background: var(--slide-footer);
  }
  .footer__name {
    position: absolute; left: 10px; top: 15px;
    font-size: 6px; font-weight: 700; color: var(--navy);
    width: 80px; line-height: 7px;
  }
  .footer__url {
    position: absolute; right: 12px; top: 17px;
    font-size: 5.5px; color: var(--muted);
  }
  .slide__title {
    position: absolute; left: 17px; top: 36px;
    font-size: 12px; font-weight: 700; color: var(--title-brown);
  }
  .slide__subtitle {
    position: absolute; left: 17px; top: 51px;
    font-size: 8.5px; color: var(--ink);
  }

  .cover__title {
    position: absolute; left: 96px; top: 82px;
    font-size: 16px; font-weight: 700; color: #fff;
  }
  .cover__subtitle {
    position: absolute; left: 96px; top: 113px;
    font-size: 10px; color: #fff;
  }
  .cover__name {
    position: absolute; left: 122px; top: 210px;
    font-size: 15px; font-weight: 700; color: var(--navy);
    line-height: 18px; width: 220px;
  }

  .bullet-list { position: absolute; list-style: none; }
  .bullet-list li {
    position: relative; padding-left: 10px; line-height: 1.35;
  }
  .bullet-list li::before {
    content: ""; position: absolute; left: 0; top: 0.45em;
    width: 4px; height: 4px; border-radius: 50%; background: var(--title-brown);
  }
  .slide--bullets .bullet-list {
    left: 30px; top: 79px; width: 225px; font-size: 7px;
  }
  .slide--bullets .bullet-list li { margin-bottom: 6px; }

  .chart {
    position: absolute; left: 17px; top: 72px; width: 331px; height: 167px;
    background: #fff;
  }
  .chart svg { display: block; }

  .section-bar {
    position: absolute; left: 9px; width: 341px; height: 15px;
    background: linear-gradient(90deg, var(--bar-dark), var(--bar-light) 70%, var(--bar-dark));
    color: #fff; font-size: 7.5px; font-weight: 700;
    padding: 3.5px 0 0 9px;
  }
  .slide--sections .bullet-list {
    left: 24px; width: 320px; font-size: 5.8px;
  }
  .slide--sections .bullet-list li { margin-bottom: 3px; }

  .body-copy {
    position: absolute; left: 40px; top: 77px; width: 300px;
    font-size: 6.6px; line-height: 1.5;
  }
  .body-copy p + p { margin-top: 10px; }

  .closing__text {
    position: absolute; left: 0; width: 100%; top: 103px; text-align: center;
    font-size: 15px; font-weight: 700; color: var(--title-brown);
  }
  .closing__rule {
    position: absolute; left: 96px; top: 125px; width: 144px; height: 1px;
    background: #c8c0b4;
  }
</style>
</head>
<body>

  <section class="slide slide--cover">
    <h1 class="cover__title">Click to add Title</h1>
    <p class="cover__subtitle">Click to add subtitle</p>
    <p class="cover__name">Ledgerwell Capital Partners</p>
  </section>

  <section class="slide slide--bullets">
    <div class="slide__topbar"></div>
    <h2 class="slide__title">Enter your title here</h2>
    <p class="slide__subtitle">Enter your subtitle here</p>
    <ul class="bullet-list">
      <li>Lorem ipsum dolor sit amet, consectetur adipisicing elit sed do eiusmod.Ut enim ad minim veniam.</li>
      <li>Lorem ipsum dolor sit ame.</li>
      <li>consectetur adipisicing elit eiusmod.Ut enim ad minim veniam.</li>
      <li>Lorem ipsum dolor sit amet, consectetur adipisicing elit sed do eiusmod.Ut enim ad minim veniam.</li>
      <li>Lorem ipsum dolor sit ame.</li>
      <li>consectetur adipisicing elit eiusmod.Ut enim ad minim veniam.</li>
    </ul>
    <footer class="slide__footer">
      <span class="footer__name">Ledgerwell Capital Partners</span>
      <span class="footer__url">www.ledgerwellcapitalpartners.example &nbsp;/&nbsp; page 1</span>
    </footer>
  </section>

  <section class="slide slide--chart">
    <div class="slide__topbar"></div>
    <h2 class="slide__title">Enter your title here</h2>
    <p class="slide__subtitle">Enter your subtitle here</p>
    <div class="chart">
      <svg width="331" height="167" viewBox="0 0 331 167" font-family="Arimo, Arial, sans-serif">
        <text x="170" y="16" font-size="10" text-anchor="middle" fill="#1a1a1a">2011 Lorem ipsum dolor sit amet</text>
        <text x="170" y="30" font-size="10" text-anchor="middle" fill="#1a1a1a">to Lorem ipsum dolor</text>
        <g stroke="var(--grid)" stroke-width="0.6">
          <line x1="24" y1="41" x2="326" y2="41"/>
          <line x1="24" y1="61" x2="326" y2="61"/>
          <line x1="24" y1="81" x2="326" y2="81"/>
          <line x1="24" y1="101" x2="326" y2="101"/>
          <line x1="24" y1="121" x2="326" y2="121"/>
          <line x1="24" y1="141" x2="326" y2="141"/>
        </g>
        <g font-size="7" fill="#1a1a1a" text-anchor="end">
          <text x="20" y="44">50%</text>
          <text x="20" y="64">40%</text>
          <text x="20" y="84">30%</text>
          <text x="20" y="104">20%</text>
          <text x="20" y="124">10%</text>
          <text x="20" y="144">0%</text>
        </g>
        <rect x="51" y="93" width="30" height="48" fill="var(--bar-blue)"/>
        <rect x="126" y="61" width="30" height="80" fill="var(--bar-red)"/>
        <rect x="200" y="91" width="30" height="50" fill="var(--bar-green)"/>
        <rect x="274" y="113" width="30" height="28" fill="var(--bar-purple)"/>
        <g font-size="6" fill="#1a1a1a" text-anchor="middle">
          <text x="66" y="152">24% Treasury Only</text>
          <text x="66" y="160">Clients</text>
          <text x="141" y="152">40% Request</text>
          <text x="141" y="160">Competitive Bank Bids</text>
          <text x="215" y="152">25% Award Treasury</text>
          <text x="215" y="160">Based on Price</text>
          <text x="289" y="152">14% Price Increases</text>
          <text x="289" y="160">Caused Bank Change</text>
        </g>
      </svg>
    </div>
    <footer class="slide__footer">
      <span class="footer__name">Ledgerwell Capital Partners</span>
      <span class="footer__url">www.ledgerwellcapitalpartners.example &nbsp;/&nbsp; page 12</span>
    </footer>
  </section>

  <section class="slide slide--sections">
    <div class="slide__topbar"></div>
    <h2 class="slide__title">Enter your title here</h2>
    <p class="slide__subtitle">Enter your subtitle here</p>
    <div class="section-bar" style="top:73px;">Enter your title here</div>
    <ul class="bullet-list" style="top:92px;">
      <li>Lorem ipsum dolor sit ame.</li>
      <li>consectetur adipisicing elit eiusmod.Ut enim ad minim veniam.<br>incididunt ut labore et dolore magna aliqua.</li>
      <li>Lorem ipsum dolor sit amet, consectetur adipisicing elit sed do eiusmod.Ut enim ad minim veniam.<br>Ut enim ad minim veniam.</li>
      <li>Lorem ipsum dolor sit amet, consectetur adipisicing elit sed do eiusmod.Ut<br>enim ad minim veniam.</li>
    </ul>
    <div class="section-bar" style="top:162px;">Enter your title here</div>
    <ul class="bullet-list" style="top:182px;">
      <li>Lorem ipsum dolor sit ame.</li>
      <li>consectetur adipisicing elit eiusmod.Ut enim ad minim veniam.<br>incididunt ut labore et dolore magna aliqua.</li>
      <li>Lorem ipsum dolor sit amet, consectetur adipisicing elit sed do eiusmod.Ut enim ad minim veniam.<br>Ut enim ad minim veniam.</li>
      <li>Lorem ipsum dolor sit amet, consectetur adipisicing elit sed do eiusmod.Ut<br>enim ad minim veniam.</li>
    </ul>
    <footer class="slide__footer">
      <span class="footer__name">Ledgerwell Capital Partners</span>
      <span class="footer__url">www.ledgerwellcapitalpartners.example &nbsp;/&nbsp; page 15</span>
    </footer>
  </section>

  <section class="slide slide--text">
    <div class="slide__topbar"></div>
    <h2 class="slide__title">Enter your title here</h2>
    <p class="slide__subtitle">Enter your subtitle here</p>
    <div class="body-copy">
      <p>Lorem ipsum dolor sit amet, consectetur adipisicing elitsed do eiusmod.Ut enim ad minim veniam.sed do eiusmod tempor incididunt ut labore et dolore magna aliqua. Ut enim ad minim veniam, quis nostrud exercitation ullamco laboris nisi ut aliquip ex ea commodo consequa.Lorem ipsum dolor sit amet, consectetur adipisicing elit, sed do eiusmod tempor incididunt ut labore et dolore magna aliqua. Ut enim ad minim veniam, quis</p>
      <p>Lorem ipsum dolor sit amet, consectetur adipisicing elitsed do eiusmod.Ut enim ad minim veniam.sed do eiusmod tempor incididunt ut labore et dolore magna aliqua. Ut enim ad minim veniam, quis nostrud exercitation ullamco laboris nisi ut aliquip ex ea commodo consequa.Lorem ipsum dolor sit amet, consectetur adipisicing elit, sed do eiusmod tempor incididunt ut labore et dolore magna aliqua. Ut enim ad minim veniam, quis</p>
    </div>
    <footer class="slide__footer">
      <span class="footer__name">Ledgerwell Capital Partners</span>
      <span class="footer__url">www.ledgerwellcapitalpartners.example &nbsp;/&nbsp; page 17</span>
    </footer>
  </section>

  <section class="slide slide--closing">
    <div class="slide__topbar"></div>
    <p class="closing__text">Thank you !</p>
    <div class="closing__rule"></div>
    <footer class="slide__footer">
      <span class="footer__name">Ledgerwell Capital Partners</span>
      <span class="footer__url">www.ledgerwellcapitalpartners.example &nbsp;/&nbsp; page 19</span>
    </footer>
  </section>

</body>
</html>
```